Company document Header needed

Using our current logo, I need a Designer to create a header for use on our company documents. This header will include our business address, phone, fax, website address
Updates

Project Deadline Extended
Reason: Dear designers, I am so pleased with the many different options that have been presented, that I wish to purchase several of them from a few different designers. I will get with the art bazaar folks and figure out what is the best way to do this. In the meantime, I am extending the deadline to allow for a few edits such as our phone number and such. thanks to you all for your excellent work. MB

Designers,

Please take a look and edit any of your submissions that have incorrect info on them:  the correct info is below:

Business name is: Tor Vale, Inc.

website address is:  www.torvale-example.com

Office #:  (855) TorVale2  

Fax#:  (858) 561-2947  (generally I do not intend to need this on any materials unless it balances a look)

email:  info@torvale-example.com

Address:  612 Harbor Rd. suite 2240  San Diego, CA  92113

Thanks!

Industry/Entity Type

Business

```html
<!DOCTYPE html>
<html lang="en">
<head>
<meta charset="utf-8">
<title>Tor Vale, Inc. — Document Header</title>
<link href="https://fonts.googleapis.com/css2?family=Josefin+Sans:wght@700&display=swap" rel="stylesheet">
<style>
  :root {
    --ink: #000000;
    --paper: #ffffff;
    --band-text: #ffffff;
  }
  * { margin: 0; padding: 0; box-sizing: border-box; }
  html, body {
    width: 1200px;
    height: 234px;
    overflow: hidden;
    background: var(--paper);
  }
  .header-canvas {
    position: relative;
    width: 1200px;
    height: 234px;
    background: var(--paper);
    font-family: "Josefin Sans", "Futura", sans-serif;
    font-weight: 700;
  }
  .header-frame {
    position: absolute;
    left: 4px;
    top: 4px;
    width: 1192px;
    height: 148px;
    border: 6px solid var(--ink);
  }
  .header-band {
    position: absolute;
    left: 150px;
    top: 23px;
    width: 900px;
    height: 114px;
    background: var(--ink);
    color: var(--band-text);
  }
  .brand-mark {
    position: absolute;
    left: 40px;
    top: 12px;
    width: 44px;
    height: 44px;
    background: var(--band-text);
  }
  .brand-name {
    position: absolute;
    left: 8px;
    top: 80px;
    font-size: 21px;
    letter-spacing: 0.5px;
    line-height: 1;
    white-space: nowrap;
  }
  .band-text {
    position: absolute;
    font-size: 17px;
    line-height: 1;
    white-space: nowrap;
  }
  .website { left: 158px; top: 86px; }
  .contact-line { left: 349px; }
  .address-line { left: 649px; }
  .line-1 { top: 58px; }
  .line-2 { top: 86px; }
</style>
</head>
<body>
  <div class="header-canvas">
    <div class="header-frame"></div>
    <header class="header-band">
      <span class="brand-mark" aria-hidden="true"></span>
      <span class="brand-name">TOR VALE</span>
      <span class="band-text website">torvale-example.com</span>
      <span class="band-text contact-line line-1">phone: 619.555.0148</span>
      <span class="band-text contact-line line-2">fax: 858.561.2947</span>
      <span class="band-text address-line line-1">612 Harbor Rd, suite 2240</span>
      <span class="band-text address-line line-2">San Diego, CA 92113</span>
    </header>
  </div>
</body>
</html>
```